vQTA Company brochure For sales and Marketing

WE need a brochure design for our company called vQTA. The logo is gold. This is an Airline Maintenace Software Company. The software it is called vQTA.

We will like the Brochure to include our modules and a brief description on what they are about.

The front cover we want to have purple night sky screen. With our logo and out motto.

The first page can have the company bio. And the inside the Company modules description.

the back can have contact Sales information.

We will like this to be modern and with style. Ower mention Perlotti catalog.

please see out sample Web Site

http://kdaran52.sitepadhub.com/vqta

Target Market(s)

Airlines

Industry/Entity Type

Airline

Requirements
Must have
• gold, black , purple, grey and chrome. we like mature scenes or night sky
Nice to have

```html
<!DOCTYPE html>
<html lang="en">
<head>
<meta charset="utf-8">
<title>vQTA Brochure – Front Cover</title>
<link rel="preconnect" href="https://fonts.googleapis.com">
<link href="https://fonts.googleapis.com/css2?family=Play:wght@400&display=swap" rel="stylesheet">
<style>
  :root {
    --backdrop: #e4e4e4;
    --night: #06050f;
    --midnight: #1a1030;
    --violet: #4b2c63;
    --dusk: #6a3f7c;
    --rose: #e7637a;
    --amber: #f4c36a;
    --cloud: #6c4a86;
    --cloud-deep: #3f2a55;
    --gold: #d4b27a;
    --silver: #e9e6ef;
  }
  * { box-sizing: border-box; margin: 0; padding: 0; }
  html, body {
    width: 1200px;
    height: 1200px;
    overflow: hidden;
    background: var(--backdrop);
  }
  .canvas {
    position: relative;
    width: 1200px;
    height: 1200px;
    display: flex;
    align-items: center;
    justify-content: center;
  }
  .cover {
    position: relative;
    width: 760px;
    height: 1075px;
    overflow: hidden;
    background: var(--night);
    box-shadow: 0 18px 40px rgba(0,0,0,0.25);
  }
  .cover-photo {
    position: absolute;
    inset: 0;
    background: linear-gradient(180deg,
      var(--night) 0%,
      var(--night) 22%,
      var(--midnight) 34%,
      var(--violet) 46%,
      var(--dusk) 53%,
      var(--rose) 58%,
      var(--amber) 63%,
      var(--cloud) 68%,
      var(--cloud) 82%,
      var(--cloud-deep) 100%);
  }
  .brand {
    position: absolute;
    top: 120px;
    right: 70px;
    text-align: right;
    font-family: "Play", sans-serif;
    font-weight: 400;
  }
  .brand-name {
    font-size: 84px;
    line-height: 1;
    color: var(--gold);
    letter-spacing: 1px;
  }
  .motto {
    margin-top: 28px;
    font-size: 19px;
    line-height: 1.3;
    color: var(--silver);
    letter-spacing: 0.3px;
  }
  .motto-highlight {
    display: block;
    font-size: 22px;
    color: var(--gold);
    letter-spacing: 1.5px;
  }
</style>
</head>
<body>
  <main class="canvas">
    <section class="cover">
      <div class="cover-photo" role="img" aria-label="Night sky photograph from an aircraft window: dark purple sky, an airliner wing silhouette, a pink and gold sunset horizon above a sea of violet clouds"></div>
      <div class="brand">
        <h1 class="brand-name">vQTA</h1>
        <p class="motto">Enterprise MRO software solution designed to for every aspect of
          <span class="motto-highlight">AIRCRAFT MAINTERNACE MANAGEMENT</span>
        </p>
      </div>
    </section>
  </main>
</body>
</html>
```